Brookside Grocer

Hope all is well!

Wanted to make business cards for my father. His name is Faisal Qureshi and owns convenience stores. I have attached logo :)

He does not want any title just simple name and phone. An email would be nice as well.

Faisal Qureshi
Cell: 413-585-2046
Store: 413-719-4820

Brooksidegrocer512@fernpost.com

The design and style is totally up to you :) The colors we were looking for were the same as logo :)

```html
<!DOCTYPE html>
<html lang="en">
<head>
<meta charset="utf-8">
<title>Brookside Grocer — Business Cards</title>
<link rel="stylesheet" href="https://fonts.googleapis.com/css2?family=Open+Sans:wght@400;700&display=swap">
<style>
  :root {
    --navy: #0f2366;
    --red: #e0141e;
    --card: #f2f2f0;
    --ink: #1a1a1a;
    --backdrop: #d6d6d6;
  }
  * { box-sizing: border-box; margin: 0; padding: 0; }
  html, body {
    width: 1200px; height: 1051px; overflow: hidden;
    background: var(--backdrop);
    font-family: "Open Sans", Arial, sans-serif;
  }
  .canvas {
    width: 1200px; height: 1051px;
    display: flex; flex-direction: column;
    align-items: center; justify-content: center; gap: 60px;
  }
  .card {
    width: 700px; height: 400px;
    background: var(--card);
    border-bottom: 6px solid var(--red);
    box-shadow: 0 18px 40px rgba(0,0,0,0.18);
    position: relative;
  }
  /* Front */
  .card--front { display: flex; align-items: center; justify-content: center; }
  .brand-name--large {
    font-weight: 700; color: var(--navy);
    font-size: 64px; letter-spacing: 1px; text-transform: uppercase;
  }
  /* Back */
  .card--back { display: flex; align-items: center; padding: 0 40px; }
  .brand-block { width: 290px; display: flex; justify-content: center; }
  .brand-name--small {
    font-weight: 700; color: var(--navy);
    font-size: 30px; text-transform: uppercase; letter-spacing: 0.5px;
    text-align: center; line-height: 1.15;
  }
  .divider { width: 2px; height: 210px; background: var(--red); margin: 0 32px 0 10px; }
  .contact { flex: 1; }
  .person-name { font-weight: 700; font-size: 28px; margin-bottom: 48px; }
  .person-name .first { color: var(--navy); }
  .person-name .last { color: var(--red); }
  .contact-list { list-style: none; font-size: 15.5px; color: var(--ink); }
  .contact-list li { display: flex; align-items: center; gap: 8px; line-height: 1.7; }
  .contact-list svg { width: 13px; height: 13px; flex: none; fill: none; stroke: var(--red); stroke-width: 2; }
  .contact-list svg.solid { fill: var(--red); stroke: none; }
</style>
</head>
<body>
<main class="canvas">
  <section class="card card--front">
    <span class="brand-name--large">Brookside Grocer</span>
  </section>

  <section class="card card--back">
    <div class="brand-block">
      <span class="brand-name--small">Brookside<br>Grocer</span>
    </div>
    <div class="divider"></div>
    <div class="contact">
      <p class="person-name"><span class="first">Faisal</span> <span class="last">Qureshi</span></p>
      <ul class="contact-list">
        <li>
          <svg viewBox="0 0 14 14" aria-hidden="true"><rect x="3.5" y="1" width="7" height="12" rx="1.2"/></svg>
          413-585-2046 (Cell)
        </li>
        <li>
          <svg class="solid" viewBox="0 0 14 14" aria-hidden="true"><path d="M3 1 L5.2 1 L6 4 L4.6 5.2 Q5.8 8 8.8 9.4 L10 8 L13 8.8 L13 11 Q12.5 13 10.5 13 Q1 12 1 3.5 Q1 1.2 3 1 Z"/></svg>
          413-719-4820 (Store)
        </li>
        <li>
          <svg class="solid" viewBox="0 0 14 14" aria-hidden="true"><path d="M1 3 H13 V11 H1 Z M1 3 L7 8 L13 3" stroke="#f2f2f0" stroke-width="1"/></svg>
          Brooksidegrocer512@fernpost.com
        </li>
      </ul>
    </div>
  </section>
</main>
</body>
</html>
```